Electrical Contractor Company Profile

We need a Brochure that is more entertaining than our current Company Profile Document. We have lots of great experience and awesome looking jobs in our portfolio but need a document that we can either print of send in electronic format to accompany some of our submissions.

We are ideally looking for something 9-10 pages in A4 with some of the pages opening out to A3.

We are looking for a document that is professional and smart however shows the colour and quality that we feel we offer to prospective clientele.

I have included the current Company Profile and Logo along with a number of images of completed projects that may be of use.

Target Market(s)

Builders, Facility Managers, Engineers, Decision makers

Industry/Entity Type

Electrical

Font styles to use
Sans Serif

Colors

Designer to choose colors to be used in the design.

Requirements
Must have
• - Modern look with a focus on sustainability
• - Clean Simple and Professional
• - Incorporate our Logo
• Core Business Lines need to be across an A3 opening page and have photos relating to these lines Solar, Communications and any of the projects.
Nice to have
• Lots of colour and photos mixed with the text
Should not have
• Lightning bolts or corny symbols

```html
<!DOCTYPE html>
<html lang="en">
<head>
<meta charset="utf-8">
<title>Brightwire Electrical Services – Company Profile Spreads</title>
<link href="https://fonts.googleapis.com/css2?family=Open+Sans:wght@400;600;700&family=Roboto+Condensed:ital,wght@0,700;1,700&family=Arimo&display=swap" rel="stylesheet">
<style>
:root{
  --board:#231f20;
  --navy:#1f4f96;
  --navy-deep:#163c78;
  --orange:#f7941d;
  --orange-deep:#e57f0e;
  --white:#ffffff;
  --label:#ffffff;
}
*{box-sizing:border-box;margin:0;padding:0}
html,body{width:1008px;height:1200px;overflow:hidden;background:var(--board)}
body{position:relative;font-family:"Open Sans",Arial,sans-serif;color:var(--white)}
.spread{position:absolute;width:432px;height:306px;display:flex}
.page{position:relative;width:216px;height:306px;background:var(--navy);overflow:hidden}
.page-label{position:absolute;font-family:"Arimo",Arial,sans-serif;font-size:19px;color:var(--label);width:216px;text-align:center}
.brand{position:absolute;top:8px;right:10px;display:flex;align-items:center;gap:4px;font-weight:700;font-size:8px;letter-spacing:.3px;color:var(--white);white-space:nowrap}
.brand .dot{width:11px;height:11px;border-radius:50%;background:var(--white)}
.rule{position:absolute;top:27px;left:0;right:0;height:1px;background:rgba(255,255,255,.75)}
.ph{position:absolute;background:linear-gradient(135deg,#6d7f92,#b9a98a 55%,#4b5866)}
.ph.warm{background:linear-gradient(135deg,#3a2f2a,#c98a3e 50%,#e9d7b4)}
.ph.sky{background:linear-gradient(180deg,#9cc3e6,#d9e4ea 55%,#7b7e5d)}
.ph.colour{background:linear-gradient(135deg,#3b4b5c,#c94f3a 35%,#e7c23a 60%,#3d8a7a)}
.ph.solar{background:linear-gradient(180deg,#a9c6df,#5f86b3 45%,#2c4a74)}
.ph.steel{background:linear-gradient(135deg,#3a3f45,#9aa3ab 50%,#d5d1c8)}
.box{position:absolute;background:var(--orange);padding:6px}
.tiny{font-size:4.4px;line-height:1.45}
.tiny p{margin-bottom:3px}
.tiny .hl{color:var(--orange);font-weight:700}
.box .tiny .hl{color:var(--navy-deep)}
.vhead{position:absolute;font-family:"Roboto Condensed",Arial,sans-serif;font-style:italic;font-weight:700;color:var(--white);writing-mode:vertical-rl;transform:rotate(180deg);white-space:nowrap}
.head{position:absolute;font-family:"Roboto Condensed",Arial,sans-serif;font-style:italic;font-weight:700;color:var(--white);line-height:.95}
.quote{font-style:italic}
.projects{position:absolute;border-collapse:collapse;font-size:3.3px;color:var(--white);table-layout:fixed}
.projects th{background:var(--navy-deep);color:var(--white);font-weight:700;padding:3px 2px;text-align:left}
.projects td{background:var(--orange);padding:2.6px 2px;border-bottom:1px solid rgba(255,255,255,.55);height:14px}
.ghost{position:absolute;font-family:"Roboto Condensed",Arial,sans-serif;font-style:italic;font-weight:700;color:rgba(255,255,255,.18);writing-mode:vertical-rl;transform:rotate(180deg);font-size:16px;white-space:nowrap}
.intro{position:absolute;font-size:4.6px;font-style:italic;color:var(--orange)}
.cover-head{position:absolute;left:0;top:0;width:216px;height:56px;background:var(--white)}
.cover-brand{position:absolute;left:22px;top:20px;display:flex;align-items:center;gap:6px;font-weight:700;font-size:13px;color:var(--navy-deep)}
.cover-brand .dot{width:20px;height:20px;border-radius:50%;background:var(--navy)}
.ticks{list-style:none}
.ticks li{position:relative;padding-left:6px;margin-bottom:1px;white-space:nowrap}
.ticks li::before{content:"";position:absolute;left:0;top:1.5px;width:2.5px;height:2.5px;background:var(--navy-deep)}
.ticks.wrap li{white-space:normal}
.ticks.light li::before{background:var(--white)}
</style>
</head>
<body>

<section class="spread" style="left:62px;top:62px">
  <div class="page back-cover">
    <div class="ph steel" style="left:0;top:34px;width:136px;height:92px" role="img" aria-label="Company service ute parked on a city street"></div>
    <div class="ph steel" style="left:140px;top:34px;width:76px;height:92px" role="img" aria-label="Service vehicle rear view with roof racks"></div>
    <div class="brand" style="left:20px;right:auto;top:208px"><span class="dot"></span>BRIGHTWIRE ELECTRICAL</div>
    <div style="position:absolute;left:20px;top:224px;width:56px;height:1px;background:rgba(255,255,255,.6)"></div>
    <div class="tiny" style="position:absolute;left:20px;top:229px;width:100px">
      <p>Licence No. EC 000000<br>Tel. 1300 000 111<br>hello@brightwire.example<br>www.brightwire.example</p>
      <p>ABN 00 000 000 000<br>12 Harbour Lane<br>Eastbank 6001<br>PO Box 100<br>Eastbank 6001</p>
    </div>
  </div>
  <div class="page front-cover" style="background:var(--navy)">
    <div class="cover-head"><div class="cover-brand"><span class="dot"></span>BRIGHTWIRE</div></div>
    <div class="ph warm" style="left:0;top:56px;width:142px;height:200px" role="img" aria-label="Colourful shopping arcade interior with mural and polished floor"></div>
    <div style="position:absolute;left:142px;top:0;width:74px;height:306px;background:var(--orange)"></div>
    <div class="vhead" style="left:176px;top:10px;font-size:20px;font-style:normal;line-height:.9">COMPANY<br>PROFILE</div>
    <svg style="position:absolute;left:0;top:236px" width="216" height="70" viewBox="0 0 216 70" aria-hidden="true">
      <path d="M0 30 Q70 10 142 20 L142 70 L0 70 Z" fill="var(--navy)"/>
    </svg>
    <div class="tiny" style="position:absolute;left:154px;top:238px;width:60px">
      <p>Licence No. EC 000000<br>Tel. 1300 000 111<br>hello@brightwire.example</p>
      <p>ABN 00 000 000 000<br>12 Harbour Lane<br>Eastbank 6001</p>
    </div>
  </div>
</section>
<div class="page-label" style="left:62px;top:374px">Back Cover Page 12</div>
<div class="page-label" style="left:278px;top:374px">Front Cover</div>

<section class="spread" style="left:516px;top:62px">
  <div class="page">
    <div class="brand"><span class="dot"></span>BRIGHTWIRE ELECTRICAL</div>
    <div class="rule"></div>
    <div class="ph sky" style="left:0;top:30px;width:216px;height:170px" role="img" aria-label="Parkside Aquatic Centre entry sign under blue sky"></div>
    <div class="box tiny" style="left:72px;top:196px;width:138px;height:82px;padding:12px 10px">
      <p>Established in 2006, Brightwire Electrical Services is an award winning business offering expertise across a broad range of electrical services including commercial, industrial and communications.</p>
      <p>We have the experience and capability to complete contracts for large and small clients with a focus on private organisations and government agencies.</p>
    </div>
  </div>
  <div class="page">
    <div class="brand"><span class="dot"></span>BRIGHTWIRE ELECTRICAL</div>
    <div class="rule"></div>
    <div class="tiny" style="position:absolute;left:8px;top:38px;width:74px">
      <p class="hl" style="font-size:5px">Our services include:</p>
      <p>-Electrical projects<br>-Planned and reactive maintenance<br>-Design and construct<br>-Electrical drafting<br>-Communications<br>-Minor works<br>-Solar generation and storage<br>-Electronic lighting control</p>
    </div>
    <div class="box tiny" style="left:84px;top:38px;width:126px;height:70px">
      <p>Brightwire enjoys a high volume of repeat business, which is a result of our:</p>
      <ul class="ticks"><li>Commitment to achieving quality results</li><li>Open dealing with clients, staff and suppliers</li><li>Ability to embrace new technologies</li><li>Staff able to complete complex projects</li><li>Proven approach to project management</li></ul>
    </div>
    <div class="ph colour" style="left:0;top:112px;width:216px;height:104px" role="img" aria-label="Arcade walkway lined with bright painted murals"></div>
    <div class="box tiny" style="left:84px;top:200px;width:126px;height:72px">
      <p>Our ability to deliver successful projects was recognised at both the 2015 and 2016 industry excellence awards, in which we received awards for best lighting and best commercial project.</p>
      <p>With an office well situated centrally in Eastbank, Brightwire is well placed to service the broader metropolitan area and regional areas throughout the state.</p>
    </div>
  </div>
</section>
<div class="page-label" style="left:516px;top:370px">Page 2</div>
<div class="page-label" style="left:732px;top:370px">Page 3</div>

<section class="spread" style="left:62px;top:430px">
  <div class="page">
    <div class="brand"><span class="dot"></span>BRIGHTWIRE ELECTRICAL</div>
    <div class="rule"></div>
    <div class="tiny" style="position:absolute;left:26px;top:40px;width:116px">
      <p>Brightwire Electrical Services maintains five core lines of business:</p>
      <p><span class="hl">1.Breakdown and response</span> – providing a 24/7 call out service to a number of high profile clients. This team is highly responsive to most situations.</p>
      <p><span class="hl">2.Planned Maintenance</span> – This team services over 500 sites across the metropolitan area, carrying out planned testing and repair.</p>
      <p><span class="hl">3.Electrical Projects</span> – This line of business is responsible for completing contracts both minor and major in value.</p>
    </div>
    <div style="position:absolute;left:146px;top:30px;width:70px;height:276px;background:var(--orange)"></div>
    <div class="vhead" style="left:172px;top:48px;font-size:15px">CORE BUSINESS</div>
    <div class="ph steel" style="left:26px;top:156px;width:190px;height:90px" role="img" aria-label="Modern white sports centre building with curved facade"></div>
    <div class="tiny quote" style="position:absolute;left:150px;top:250px;width:62px">"The finished product at the Coastal Sports Centre was of excellent quality. We were extremely impressed." Dana Pryor, Halden Builders</div>
  </div>
  <div class="page">
    <div class="brand"><span class="dot"></span>BRIGHTWIRE ELECTRICAL</div>
    <div class="rule"></div>
    <div style="position:absolute;left:0;top:30px;width:70px;height:276px;background:var(--orange)"></div>
    <div class="vhead" style="left:26px;top:48px;font-size:15px">CORE BUSINESS</div>
    <div class="tiny" style="position:absolute;left:78px;top:40px;width:126px">
      <p><span class="hl">4.Communications</span> – our staff are extensively experienced and the majority carry open cabling licences. The company owns specialised test equipment.</p>
      <p><span class="hl">5.Solar PV</span> – Focusing on the commercial market we offer fully designed photovoltaic systems up to 200kW to suit a client's needs and budget.</p>
      <p><span class="hl">6.Technology Services</span> – With great base knowledge and ongoing training we offer solutions for energy management, lighting control and performance auditing.</p>
    </div>
    <div class="tiny quote" style="position:absolute;left:8px;top:196px;width:58px">"The finished product is of excellent quality and we have been extremely impressed with the ease of use." Lee Hart, Ardent Homes</div>
    <div class="ph warm" style="left:70px;top:176px;width:146px;height:100px" role="img" aria-label="Switchboard interior with orange cabling"></div>
  </div>
</section>
<div class="page-label" style="left:62px;top:742px">Page 4</div>
<div class="page-label" style="left:278px;top:742px">Page 5</div>

<section class="spread" style="left:516px;top:434px">
  <div class="page">
    <div class="brand"><span class="dot"></span>BRIGHTWIRE ELECTRICAL</div>
    <div class="rule"></div>
    <div class="ph colour" style="left:0;top:30px;width:216px;height:148px" role="img" aria-label="Ceiling installation of hanging coloured light rods"></div>
    <div class="head" style="left:10px;top:40px;font-size:13px;font-style:normal">PROVEN<br>MANAGEMENT<br>SYSTEMS</div>
    <div class="tiny quote" style="position:absolute;left:10px;top:84px;width:90px;font-weight:700">Our commitment to quality, health and safety and the environment places us apart from our many competitors.</div>
    <div class="tiny quote" style="position:absolute;left:10px;top:184px;width:66px">"We found them to be professional, courteous and able to carry out their works both on time and on budget." Dana Pryor, Halden Builders</div>
    <div class="box" style="left:86px;top:178px;width:126px;height:116px">
      <div class="vhead" style="left:2px;top:4px;font-size:14px">QUALITY</div>
      <div class="tiny" style="position:absolute;left:24px;top:6px;width:96px">
        <p>Brightwire is committed to providing clients with exceptional products and services in a creative and innovative manner. Our integrated management system ensures a consistent result.</p>
        <p>-Consistent communication with stakeholders<br>-Experienced and qualified staff<br>-A flexible workforce across all areas<br>-Internal systems for thorough reporting<br>-Clearly defined roles for all staff<br>-Continued training and support</p>
      </div>
    </div>
  </div>
  <div class="page">
    <div class="brand"><span class="dot"></span>BRIGHTWIRE ELECTRICAL</div>
    <div class="rule"></div>
    <div class="box" style="left:0;top:36px;width:132px;height:90px">
      <div class="head" style="left:36px;top:2px;font-size:12px">ENVIRONMENT</div>
      <div class="tiny" style="position:absolute;left:14px;top:18px;width:108px">Brightwire seeks to deliver all projects in an environmentally responsible manner. We have a comprehensive set of policies and procedures that ensure we comply with all relevant environmental legislation, regulations and codes of practice. We only conduct business with suppliers who share a commitment to responsible environmental management.</div>
    </div>
    <div class="ph solar" style="left:132px;top:36px;width:84px;height:90px" role="img" aria-label="Rooftop solar panel array"></div>
    <div class="box" style="left:14px;top:132px;width:118px;height:10px;padding:1px 4px"><div class="head" style="position:static;font-size:6px">WORKPLACE HEALTH AND SAFETY</div></div>
    <div class="tiny" style="position:absolute;left:14px;top:145px;width:118px">
      <p class="hl" style="font-size:5px;font-style:italic;margin-bottom:1px">Our high level of safety is achieved by:</p>
      <ul class="ticks light"><li>Planning and monitoring a safety programme</li><li>Promoting health, safety and welfare</li><li>Developing site specific plans</li><li>Ensuring staff receive proper training</li><li>Providing a healthy and safe workplace</li></ul>
    </div>
    <div class="box tiny" style="left:138px;top:134px;width:72px;height:70px;background:var(--orange)">
      <div class="brand" style="position:static;font-size:5px;margin-bottom:4px"><span class="dot" style="width:7px;height:7px"></span>BRIGHTWIRE</div>
      Within a comprehensive safety management system, developed with industry bodies and tailored to suit the business, the system is:<br>Certified to the current safety standard
    </div>
    <div class="tiny quote hl" style="position:absolute;left:142px;top:210px;width:68px;font-weight:700">Our system is audited twice annually to ensure that the system is being utilised</div>
    <div class="ph warm" style="left:14px;top:196px;width:118px;height:66px" role="img" aria-label="Covered outdoor dining terrace with timber roof at dusk"></div>
    <div class="box tiny quote" style="left:14px;top:262px;width:118px;height:34px">"We have a long history on various projects and have been extremely satisfied with the levels of quality and service." Marco Vell, Ridgeline Construct</div>
  </div>
</section>
<div class="page-label" style="left:516px;top:742px">Page 6</div>
<div class="page-label" style="left:732px;top:742px">Page 7</div>

<section class="spread" style="left:62px;top:800px">
  <div class="page">
    <div class="brand"><span class="dot"></span>BRIGHTWIRE ELECTRICAL</div>
    <div class="rule"></div>
    <div class="intro" style="left:36px;top:42px;width:170px">Brightwire Electrical Services has been pleased to complete the following projects:</div>
    <div class="ghost" style="left:20px;top:60px">DELIVERED PROJECTS</div>
    <table class="projects" style="left:36px;top:58px;width:170px">
      <colgroup><col style="width:30%"><col style="width:18%"><col style="width:30%"><col style="width:11%"><col style="width:11%"></colgroup>
      <tr><th>PROJECT</th><th>CATEGORY</th><th>DESCRIPTION</th><th>YEAR</th><th>VALUE</th></tr>
      <tr><td>Harbour Hotel</td><td>Retail</td><td>New 4 storey hotel fit-out</td><td>2016</td><td>1.8M</td></tr>
      <tr><td>Northgate School</td><td>Education</td><td>New teaching and admin block</td><td>2016</td><td>1.2M</td></tr>
      <tr><td>South Bay College</td><td>Education</td><td>Site power upgrade</td><td>2016</td><td>1.0M</td></tr>
      <tr><td>St Clare College</td><td>Education</td><td>Multiple new teaching blocks</td><td>2016</td><td>1.4M</td></tr>
      <tr><td>Beacon Street Housing</td><td>Residential</td><td>Ten storey housing block</td><td>2016</td><td>1.6M</td></tr>
      <tr><td>Rescue Centre</td><td>Commercial</td><td>New headquarters</td><td>2015</td><td>800K</td></tr>
      <tr><td>Transit Centre</td><td>Commercial</td><td>Supply and distribution upgrade</td><td>2015</td><td>1.4M</td></tr>
      <tr><td>Coastal Sports Centre</td><td>Commercial</td><td>Multi-function training centre</td><td>2015</td><td>1.9M</td></tr>
      <tr><td>Lakeside Apartments</td><td>Residential</td><td>Boutique townhouses</td><td>2015</td><td>1.4M</td></tr>
      <tr><td>Hillview Shopping Centre</td><td>Retail</td><td>Distribution upgrade to shops</td><td>2014</td><td>450K</td></tr>
      <tr><td>Riverside Brewery</td><td>Commercial</td><td>Production centre and tavern</td><td>2014</td><td>1.0M</td></tr>
      <tr><td>Kingsway College</td><td>Education</td><td>Extension of teaching block</td><td>2014</td><td>500K</td></tr>
      <tr><td>Westwood College</td><td>Education</td><td>Multi-function sports hall</td><td>2014</td><td>1.1M</td></tr>
      <tr><td>Early Learning Centre</td><td>Education</td><td>New teaching block</td><td>2014</td><td>350K</td></tr>
    </table>
  </div>
  <div class="page">
    <div class="brand"><span class="dot"></span>BRIGHTWIRE ELECTRICAL</div>
    <div class="rule"></div>
    <div class="ph steel" style="left:4px;top:36px;width:60px;height:56px" role="img" aria-label="Office interior with suspended lighting"></div>
    <div class="ph warm" style="left:68px;top:36px;width:144px;height:56px" role="img" aria-label="Restaurant interior with timber ceiling"></div>
    <div class="ph steel" style="left:4px;top:96px;width:122px;height:86px" role="img" aria-label="Curved timber-clad building facade"></div>
    <div class="ph colour" style="left:130px;top:96px;width:82px;height:86px" role="img" aria-label="Coloured pendant light installation"></div>
    <div class="ph colour" style="left:4px;top:186px;width:72px;height:56px" role="img" aria-label="Arcade mural walkway"></div>
    <div class="ph sky" style="left:80px;top:186px;width:70px;height:56px" role="img" aria-label="Aquatic centre sign and trees"></div>
    <div class="ph solar" style="left:154px;top:186px;width:58px;height:56px" role="img" aria-label="Solar panels on roof"></div>
    <div style="position:absolute;left:4px;top:246px;width:146px;height:42px;background:var(--white);display:flex;align-items:center;justify-content:center;gap:6px;font-weight:700;font-size:14px;color:var(--navy-deep)"><span style="width:22px;height:22px;border-radius:50%;background:var(--navy)"></span>BRIGHTWIRE</div>
    <div class="ph colour" style="left:154px;top:246px;width:58px;height:42px" role="img" aria-label="Colourful light rod ceiling detail"></div>
  </div>
</section>
<div class="page-label" style="left:62px;top:1114px">Page 8</div>
<div class="page-label" style="left:278px;top:1114px">Page 9</div>

<section class="spread" style="left:516px;top:803px">
  <div class="page">
    <div class="brand"><span class="dot"></span>BRIGHTWIRE ELECTRICAL</div>
    <div class="rule"></div>
    <div class="intro" style="left:36px;top:42px;width:170px">Brightwire Electrical Services has been pleased to complete the following projects:</div>
    <div class="ghost" style="left:20px;top:60px">DELIVERED PROJECTS</div>
    <table class="projects" style="left:36px;top:58px;width:170px">
      <colgroup><col style="width:30%"><col style="width:18%"><col style="width:30%"><col style="width:11%"><col style="width:11%"></colgroup>
      <tr><th>PROJECT</th><th>CATEGORY</th><th>DESCRIPTION</th><th>YEAR</th><th>VALUE</th></tr>
      <tr><td>Community College</td><td>Education</td><td>New teaching block</td><td>2014</td><td>750K</td></tr>
      <tr><td>Market Square</td><td>Retail</td><td>Upgrade of retail arcade</td><td>2014</td><td>1.6M</td></tr>
      <tr><td>Marina Apartments</td><td>Residential</td><td>Multi storey apartment block</td><td>2014</td><td>2.5M</td></tr>
      <tr><td>Parkside Clinic</td><td>Health</td><td>New consulting rooms</td><td>2013</td><td>1.2M</td></tr>
      <tr><td>Youth Centre</td><td>Commercial</td><td>Multi-storey youth facility</td><td>2013</td><td>2.0M</td></tr>
      <tr><td>City Art Gallery</td><td>Commercial</td><td>Lighting upgrade to gallery</td><td>2013</td><td>600K</td></tr>
      <tr><td>Trade Training Centre</td><td>Education</td><td>Plumbing trade training</td><td>2013</td><td>700K</td></tr>
      <tr><td>Avenue Place</td><td>Retail</td><td>New shopping centre fit-out</td><td>2013</td><td>1.4M</td></tr>
      <tr><td>Promenade Apartments</td><td>Residential</td><td>Boutique apartments</td><td>2013</td><td>400K</td></tr>
      <tr><td>Valley Imaging House</td><td>Health</td><td>New medical imaging facility</td><td>2013</td><td>800K</td></tr>
      <tr><td>Port Rose Building</td><td>Residential</td><td>Multi storey units</td><td>2012</td><td>1.5M</td></tr>
      <tr><td>Bayside Raceway</td><td>Commercial</td><td>Media and viewing upgrade</td><td>2012</td><td>1.7M</td></tr>
      <tr><td>Ridge School</td><td>Education</td><td>Site power supply upgrade</td><td>2012</td><td>1.0M</td></tr>
      <tr><td>Innovation Hub</td><td>Commercial</td><td>Commercial build and fit-out</td><td>2012</td><td>2.9M</td></tr>
      <tr><td>Technology Institute</td><td>Education</td><td>Teaching facility and offices</td><td>2011</td><td>400K</td></tr>
    </table>
  </div>
  <div class="page">
    <div class="brand"><span class="dot"></span>BRIGHTWIRE ELECTRICAL</div>
    <div class="rule"></div>
    <div class="ph warm" style="left:0;top:30px;width:216px;height:276px;background:linear-gradient(180deg,#f2a23b,#efc178 25%,#8d8a84 55%,#3b3f45)" role="img" aria-label="Brewery hall with copper pendant lights and steel tanks"></div>
    <div class="tiny quote" style="position:absolute;left:90px;top:42px;width:118px;color:var(--navy-deep);font-weight:600">"The final quality of workmanship on the brewery is a reflection of the commitment that Brightwire applies to all its projects." Marco Vell, Ridgeline Construct</div>
    <div class="box" style="left:80px;top:186px;width:136px;height:110px">
      <div class="vhead" style="left:2px;top:4px;font-size:14px">SUMMARY</div>
      <div class="tiny" style="position:absolute;left:24px;top:14px;width:106px">
        <p>Brightwire Electrical Services is an award winning company that offers:</p>
        <ul class="ticks wrap"><li>Experience with a broad range of projects</li><li>An innovative approach</li><li>Experienced and knowledgeable staff</li><li>Thorough project planning</li><li>Strong operational systems</li><li>Effective communication with everyone</li><li>A commitment to quality workmanship. We look forward to working on your project.</li></ul>
      </div>
    </div>
  </div>
</section>
<div class="page-label" style="left:516px;top:1111px">Page 10</div>
<div class="page-label" style="left:732px;top:1111px">Page 11</div>

</body>
</html>
```